Mineral Drinking Water Label Design

We need a label design for a new bottled drinking water based in (either Pwani or Dar Es Salaam, decision is not yet finalized), Tanzania on the coast of East Africa.

We will use underground aquifers as our only source of raw water(pre treated water).

Which will then be treated through osmosis process, then the mineral water will be bottled in standard 500ml, 1000ml and 1500 ml plastic PET bottles for customer consumption.

We have a vision of expanding our supply network to cover the entire country. Therefore, we expect the label to communicate trust, purity, cleanliness, healthiness of water contained.

The uniqueness and attractiveness of the label/logo is of utmost importance.

With regards to water brand name, we prefer that you use your own imagination and creativity to come up with a name that might be more suited to your individual design.

Note: Different shades of blue are mainly associated with drinking water in Tanzania, however feel free to use any other colors.

Target Market(s)

Upper Class citizens, Hotels, Large Supermarkets etc

Font styles to use
Script

Colors

Designer to choose colors to be used in the design.

```html
<!DOCTYPE html>
<html lang="en">
<head>
<meta charset="utf-8">
<title>Neema Aqua – Bottle Labels</title>
<link href="https://fonts.googleapis.com/css2?family=Lobster&family=Archivo:wght@400;800&family=Roboto+Condensed:wght@400;700&display=swap" rel="stylesheet">
<style>
  :root {
    --canvas: #e9eaec;
    --label-white: #ffffff;
    --label-mist: #dcebf7;
    --brand-blue: #2a7fd0;
    --splash-deep: #2f7fb0;
    --splash-mid: #7fb7d8;
    --splash-light: #d9ecf7;
    --tag-bg: #0b0f14;
    --tag-text: #38c6f0;
    --ink: #1b1b1b;
    --ink-soft: #555;
  }
  * { box-sizing: border-box; margin: 0; padding: 0; }
  html, body { width: 1050px; height: 1200px; overflow: hidden; }
  body { background: var(--canvas); position: relative; font-family: "Roboto Condensed", sans-serif; }

  .front-label {
    position: absolute; left: 50px; top: 380px; width: 500px; height: 410px;
    background: linear-gradient(180deg, var(--label-white) 0%, #f6f9fb 60%, var(--label-mist) 100%);
    overflow: hidden;
    box-shadow: 0 2px 8px rgba(0,0,0,.08);
  }
  .front-label .splash {
    position: absolute; left: 0; right: 0; bottom: 0; height: 250px;
    background:
      radial-gradient(ellipse 60% 55% at 30% 75%, var(--splash-deep) 0%, transparent 70%),
      radial-gradient(ellipse 45% 50% at 85% 70%, var(--splash-deep) 0%, transparent 70%),
      linear-gradient(180deg, rgba(255,255,255,0) 0%, var(--splash-light) 35%, var(--splash-mid) 100%);
  }
  .brand-name {
    position: absolute; left: 0; right: 0; top: 30px;
    font-family: "Lobster", cursive; font-weight: 400; color: var(--brand-blue);
    line-height: .9;
  }
  .brand-name .brand-top { display: block; font-size: 80px; padding-left: 205px; }
  .brand-name .brand-main { display: block; font-size: 160px; padding-left: 40px; }
  .volume-tag {
    position: absolute; right: 22px; bottom: 34px;
    background: var(--tag-bg); color: var(--tag-text);
    font-family: "Roboto Condensed", sans-serif; font-size: 20px; padding: 1px 5px;
  }

  .back-label {
    position: absolute; left: 610px; top: 400px; width: 390px; height: 380px;
    background: linear-gradient(180deg, var(--label-white) 0%, #f3f8fb 55%, var(--label-mist) 100%);
    box-shadow: 0 2px 8px rgba(0,0,0,.08);
  }
  .nutrition-panel {
    position: absolute; left: 40px; top: 0; width: 280px;
    border: 3px solid var(--ink); background: var(--label-white);
    padding: 7px 8px 8px; color: var(--ink);
  }
  .nutrition-title { font-family: "Archivo", sans-serif; font-weight: 800; font-size: 26px; line-height: 1; }
  .nutrition-source { font-size: 12px; color: var(--ink-soft); margin-top: 3px; }
  .serving { display: flex; align-items: center; gap: 6px; font-size: 12px; margin-top: 5px; color: var(--ink-soft); }
  .serving .serving-box { border: 1px solid #999; padding: 0 5px; }
  .rule-thick { height: 10px; background: var(--ink); margin: 8px 0 3px; }
  .rule-mid { height: 6px; background: var(--ink); margin: 5px 0 3px; }
  .row { display: flex; justify-content: space-between; font-size: 12px; line-height: 14px; padding: 2px 0; border-bottom: 1px solid var(--ink); }
  .row.bold { font-weight: 700; }
  .row.plain { border-bottom: none; }
  .row.right { justify-content: flex-end; font-weight: 700; }
  .footnote { font-size: 10.5px; color: var(--ink-soft); margin-top: 10px; line-height: 1.3; }
  .bin-icon { position: absolute; left: 340px; top: 285px; width: 28px; height: 34px; }
</style>
</head>
<body>
  <section class="front-label">
    <div class="splash" role="img" aria-label="Blue water splash illustration"></div>
    <h1 class="brand-name"><span class="brand-top">Neema</span><span class="brand-main">Aqua</span></h1>
    <span class="volume-tag">1.Litre</span>
  </section>

  <section class="back-label">
    <div class="nutrition-panel">
      <h2 class="nutrition-title">Nutrition Facts</h2>
      <p class="nutrition-source">Natural Spring Water - From Ruvu Springs</p>
      <div class="serving"><span class="serving-box">330</span> ml</div>
      <div class="rule-thick"></div>
      <div class="row bold"><span>Amount Per Serving</span></div>
      <div class="row plain"><span>Calories 0</span></div>
      <div class="rule-mid"></div>
      <div class="row right"><span>% Daily Value*</span></div>
      <div class="row"><span><b>Total Fat</b> 0g</span><span>0%</span></div>
      <div class="row"><span><b>Total Carbohydrates</b> 0g</span><span>0%</span></div>
      <div class="row plain"><span><b>Protein</b> 0g</span></div>
      <div class="rule-thick"></div>
      <div class="row plain"><span>Calcium</span><span>2%</span></div>
      <p class="footnote">* Percent Daily Values are based on a 2000 calorie diet. Your Daily Values may be higher or lower depending on your calorie needs.</p>
    </div>
    <svg class="bin-icon" viewBox="0 0 28 34" aria-label="Dispose in bin">
      <circle cx="21" cy="4" r="3" fill="#1b1b1b"/>
      <path d="M21 8 L19 20 L22 32 M19 14 L13 10 M20 20 L16 32" stroke="#1b1b1b" stroke-width="2.4" fill="none" stroke-linecap="round"/>
      <path d="M2 18 H13 L11.5 32 H3.5 Z" fill="none" stroke="#1b1b1b" stroke-width="1.6"/>
      <path d="M5 21 V29 M7.5 21 V29 M10 21 V29" stroke="#1b1b1b" stroke-width="1"/>
    </svg>
  </section>
</body>
</html>
```